Bright Oak Fitness Facility Business Cards

Business Card Design that incorporates the logo and tagline

Target Market(s)

Fitness, People Who Exercise

Contact Information for Business Card

2817 Mossgrove Bend Road
Cedar Hollow, Ohio 43190
Phone: 740-555-Jump (5867)
www.brightoakfitness.example
info@brightoakfitness.example

Requirements
Must have
• Logo, Address, Website, email and tagline "More Than A Gym". Colors should be red/black/grey/white

```html
<!DOCTYPE html>
<html lang="en">
<head>
<meta charset="utf-8">
<title>Bright Oak Fitness – Business Cards</title>
<link rel="stylesheet" href="https://fonts.googleapis.com/css2?family=Jost:wght@400;500&family=Source+Sans+3:wght@400&display=swap">
<style>
  :root {
    --stage: #151515;
    --card-dark: #1f1d1d;
    --card-red: #e0252b;
    --brand-red: #e31e26;
    --white: #ffffff;
    --paper: #f1f1f1;
    --grey-light: #dedede;
    --grey-mid: #a9a9a9;
    --rule-dark: rgba(255,255,255,0.28);
    --rule-red: rgba(255,255,255,0.45);
  }
  * { margin: 0; padding: 0; box-sizing: border-box; }
  html, body { width: 1200px; height: 1074px; overflow: hidden; background: var(--stage); }
  .canvas { position: relative; width: 1200px; height: 1074px; }

  .card {
    position: absolute; left: 232px; width: 730px; height: 419px;
    border-radius: 26px; overflow: hidden;
  }
  .card--dark { top: 114px; background: var(--card-dark); }
  .card--red { top: 576px; background: var(--card-red); }

  .name-band {
    position: absolute; left: 0; top: 90px; width: 326px; height: 71px;
    padding: 9px 0 0 22px; font-family: "Jost", sans-serif;
  }
  .name-band__title { font-size: 31px; font-weight: 400; line-height: 34px; letter-spacing: -0.5px; white-space: nowrap; }
  .name-band__tagline { font-size: 15px; font-weight: 400; line-height: 18px; }
  .card--dark .name-band { background: var(--brand-red); color: var(--white); }
  .card--red .name-band { background: var(--paper); color: var(--brand-red); }

  .brand-mark {
    position: absolute; left: 430px; top: 88px; width: 240px;
    font-family: "Jost", sans-serif; font-weight: 500; font-size: 32px;
    line-height: 36px; text-align: center; letter-spacing: 1px;
  }
  .card--dark .brand-mark { color: var(--brand-red); }
  .card--red .brand-mark { color: var(--white); }

  .divider { position: absolute; left: 0; right: 0; top: 226px; height: 1px; }
  .card--dark .divider { background: var(--rule-dark); }
  .card--red .divider { background: var(--rule-red); }

  .contact-list {
    position: absolute; left: 26px; top: 266px; list-style: none;
    font-family: "Source Sans 3", sans-serif; font-size: 18px; line-height: 23px;
  }
  .contact-list li { display: flex; align-items: center; white-space: nowrap; }
  .contact-list svg { width: 14px; height: 14px; margin-right: 20px; flex: none; }
  .address {
    position: absolute; left: 474px; top: 272px; display: flex;
    font-family: "Source Sans 3", sans-serif; font-size: 18px; line-height: 23px;
    white-space: nowrap;
  }
  .address svg { width: 14px; height: 18px; margin: 3px 14px 0 0; flex: none; }

  .card--dark .contact-list, .card--dark .address { color: var(--grey-light); }
  .card--dark .contact-list .email, .card--dark .address .city { color: var(--grey-mid); }
  .card--dark .icon { fill: none; stroke: var(--brand-red); }
  .card--dark .icon-fill { fill: var(--brand-red); }
  .card--red .contact-list, .card--red .address { color: var(--white); }
  .card--red .icon { fill: none; stroke: var(--white); }
  .card--red .icon-fill { fill: var(--white); }
</style>
</head>
<body>
<main class="canvas">

  <section class="card card--dark" aria-label="Business card, dark side">
    <div class="name-band">
      <p class="name-band__title">BRIGHTOAK FITNESS</p>
      <p class="name-band__tagline">MORE THAN A GYM</p>
    </div>
    <p class="brand-mark">BRIGHT OAK<br>FITNESS</p>
    <div class="divider"></div>
    <ul class="contact-list">
      <li><svg viewBox="0 0 14 14"><rect class="icon" x="4" y="1" width="6" height="12" rx="1" stroke-width="1.4"/></svg>Phone: 740-555-Jump (5867)</li>
      <li><svg viewBox="0 0 14 14"><circle class="icon" cx="7" cy="7" r="5.5" stroke-width="1.3"/><path class="icon" d="M1.5 7h11M7 1.5c-3 3.5-3 7.5 0 11M7 1.5c3 3.5 3 7.5 0 11" stroke-width="1"/></svg>www.brightoakfitness.example</li>
      <li class="email"><svg viewBox="0 0 14 14"><rect class="icon" x="1" y="3" width="12" height="8" stroke-width="1.3"/><path class="icon" d="M1 3l6 5 6-5" stroke-width="1.3"/></svg>info@brightoakfitness.example</li>
    </ul>
    <div class="address">
      <svg viewBox="0 0 14 18"><path class="icon-fill" d="M7 0a6 6 0 0 0-6 6c0 4.5 6 12 6 12s6-7.5 6-12a6 6 0 0 0-6-6zm0 8.5a2.5 2.5 0 1 1 0-5 2.5 2.5 0 0 1 0 5z"/></svg>
      <p>2817 Mossgrove Bend Road<br><span class="city">Cedar Hollow, Ohio 43190</span></p>
    </div>
  </section>

  <section class="card card--red" aria-label="Business card, red side">
    <div class="name-band">
      <p class="name-band__title">BRIGHTOAK FITNESS</p>
      <p class="name-band__tagline">MORE THAN A GYM</p>
    </div>
    <p class="brand-mark">BRIGHT OAK<br>FITNESS</p>
    <div class="divider"></div>
    <ul class="contact-list">
      <li><svg viewBox="0 0 14 14"><rect class="icon" x="4" y="1" width="6" height="12" rx="1" stroke-width="1.4"/></svg>Phone: 740-555-Jump (5867)</li>
      <li><svg viewBox="0 0 14 14"><circle class="icon" cx="7" cy="7" r="5.5" stroke-width="1.3"/><path class="icon" d="M1.5 7h11M7 1.5c-3 3.5-3 7.5 0 11M7 1.5c3 3.5 3 7.5 0 11" stroke-width="1"/></svg>www.brightoakfitness.example</li>
      <li class="email"><svg viewBox="0 0 14 14"><rect class="icon" x="1" y="3" width="12" height="8" stroke-width="1.3"/><path class="icon" d="M1 3l6 5 6-5" stroke-width="1.3"/></svg>info@brightoakfitness.example</li>
    </ul>
    <div class="address">
      <svg viewBox="0 0 14 18"><path class="icon-fill" d="M7 0a6 6 0 0 0-6 6c0 4.5 6 12 6 12s6-7.5 6-12a6 6 0 0 0-6-6zm0 8.5a2.5 2.5 0 1 1 0-5 2.5 2.5 0 0 1 0 5z"/></svg>
      <p>2817 Mossgrove Bend Road<br><span class="city">Cedar Hollow, Ohio 43190</span></p>
    </div>
  </section>

</main>
</body>
</html>
```